Leaf Lattice Logo, Icons and web design

Looking for a new logo for the Sprout Sage, and a set of 12-15 icons and color scheme (and a few sample pages) to include some creative, but clean and professional content boxes. The current site is http://www.leaflattice-demo.com. We would like to see logo variants - both based on the current design, as well as some new creative options.
Leaf Lattice is a SaaS website designed for the green industry participants who want to save trees during construction or other land disturbances (landscape architects, builders/developers, architects, homeowners). It features a patented algorithm to predict tree survival. We also offer the Sprout Sage to find the best plant for the planting location.

We would like to see a page with embedded video for our promotional and tutorial videos.

Specifically we would to see icons for two services:

Leaf Lattice: A root plotting tree survival prediction tool
https://www.leaflattice-demo.com/how-root-keeper-works

Our Sprout Sage: https://www.leaflattice-demo.com/how-sprout-sage-works
The current site is based on a twitter bootstrap 4.0 template, so this is strongly preferred.

Target Market(s)

Landscape architects, builders and developer as well as municipal tree planning and preservation specialists.

Coding

Coded - Design and coding required

Number of Pages Required

4 page

Font styles to use
Sans Serif

```html
<!DOCTYPE html>
<html lang="en">
<head>
<meta charset="utf-8">
<title>Leaf Lattice</title>
<link href="https://fonts.googleapis.com/css2?family=Inter:wght@400;500;600&family=Rubik:wght@500;600;700&family=Roboto+Slab:wght@500&display=swap" rel="stylesheet">
<style>
:root{
  --green:#0c6a0c;
  --logo-green:#4b6b3c;
  --nav-green:#3f5a31;
  --orange:#ef8f1c;
  --text:#333333;
  --muted:#555555;
  --grey-band:#eeeeee;
  --white:#ffffff;
  --dark-card:#333333;
}
*{margin:0;padding:0;box-sizing:border-box}
html,body{width:1200px;height:2675px;overflow:hidden;background:var(--white)}
body{position:relative;font-family:"Inter",sans-serif;color:var(--text)}
.abs{position:absolute}

/* header */
.site-header{position:absolute;left:0;top:0;width:1200px;height:88px;background:var(--white)}
.brand{position:absolute;left:114px;top:22px;display:flex;align-items:center;gap:10px;
  font-family:"Roboto Slab",serif;font-weight:500;font-size:25px;color:var(--logo-green)}
.brand-dot{width:34px;height:34px;border-radius:50%;background:var(--logo-green)}
.main-nav{position:absolute;top:32px;left:706px;display:flex;gap:27px;
  font-family:"Rubik",sans-serif;font-weight:600;font-size:15px;color:var(--nav-green)}

/* hero */
.hero{position:absolute;left:0;top:88px;width:1200px;height:603px;
  background:radial-gradient(ellipse at 55% 55%,#6f8a2c 0%,#4f6b26 35%,#2f4319 70%,#1f2c12 100%)}
.hero-kicker{position:absolute;top:250px;width:100%;text-align:center;color:var(--white);font-size:18px}
.hero-title{position:absolute;top:274px;width:100%;text-align:center;color:var(--white);
  font-family:"Rubik",sans-serif;font-weight:700;font-size:46px}
.btn{display:inline-flex;align-items:center;justify-content:center;font-size:15px;border-radius:2px;white-space:nowrap}
.btn-orange{background:var(--orange);color:var(--white)}
.btn-ghost{background:var(--white);color:var(--orange);border:1px solid #ddd}
.hero-arrow{position:absolute;top:290px;color:rgba(255,255,255,.7);font-size:26px}
.hero-dots{position:absolute;top:574px;left:596px;display:flex;gap:5px}
.hero-dots span{width:4px;height:4px;border-radius:50%;background:rgba(255,255,255,.9)}
.hero-dots span+span{background:rgba(255,255,255,.4)}

/* intro */
.intro{position:absolute;left:0;top:691px;width:1200px;height:1400px;background:#fafafa}
.section-title{font-family:"Rubik",sans-serif;font-weight:600;font-size:37px;color:var(--green)}
.intro-text{position:absolute;width:1000px;left:100px;text-align:center;font-size:16px;line-height:26.5px;color:var(--text)}
.feature{position:absolute;top:1000px;width:160px;text-align:center}
.feature svg{display:block;margin:0 auto}
.feature p{margin-top:24px;font-size:14.5px;font-weight:500;line-height:29px;color:var(--text)}

/* cards */
.card{position:absolute;top:1539px;width:309px;height:414px;background:var(--white);text-align:center}
.card svg{position:absolute;top:32px;left:50%;transform:translateX(-50%)}
.card h3{position:absolute;top:104px;width:100%;font-family:"Rubik",sans-serif;font-weight:600;font-size:16.5px;color:var(--green)}
.card p{position:absolute;top:146px;left:14px;right:14px;font-size:14px;line-height:29px;color:var(--muted)}
.card .actions{position:absolute;top:331px;width:100%;display:flex;justify-content:center;gap:8px}
.card .btn{height:47px;padding:0 27px}

/* audience */
.audience{position:absolute;left:0;top:2088px;width:1200px;height:343px;
  background:linear-gradient(90deg,#3a2a1c 0%,#5b3a22 30%,#4a3020 60%,#2e3a1c 100%)}
.audience-title{position:absolute;top:2148px;width:100%;text-align:center;color:var(--white);
  font-family:"Rubik",sans-serif;font-weight:600;font-size:37px}
.planner-card{position:absolute;left:29px;top:2237px;width:347px;height:374px;background:var(--dark-card);color:var(--white);
  box-shadow:0 10px 20px rgba(0,0,0,.15)}
.planner-card h3{position:absolute;top:42px;width:100%;text-align:center;font-weight:400;font-size:25px}
.planner-card ul{position:absolute;top:126px;left:34px;list-style:none}
.planner-card li{font-size:13.5px;height:44px;display:flex;gap:8px;white-space:nowrap}
.photo{position:absolute;top:2237px;height:379px}
</style>
</head>
<body>

<header class="site-header">
  <div class="brand"><span class="brand-dot"></span>Leaf Lattice</div>
  <nav class="main-nav"><span>Our Products</span><span>Tutorial</span><span>See Demo</span><span>Contact</span></nav>
</header>

<section class="hero" role="img" aria-label="Photograph of a sunlit pine forest with a mossy path">
  <div class="hero-arrow" style="left:84px">&#8249;</div>
  <div class="hero-arrow" style="left:1106px">&#8250;</div>
  <p class="hero-kicker">Take the Uncertainty</p>
  <h1 class="hero-title">Out of Tree Preservations</h1>
  <div class="abs" style="top:359px;left:459px;display:flex;gap:16px;align-items:center">
    <span class="btn btn-ghost" style="width:144px;height:48px">Get Free Trial</span>
    <span class="btn btn-orange" style="width:128px;height:55px">Know More</span>
  </div>
  <div class="hero-dots"><span></span><span></span></div>
</section>

<section class="intro">
  <svg class="abs" style="left:0;top:0" width="1200" height="1400" viewBox="0 0 1200 1400">
    <path d="M0 515 C300 540 700 680 1200 770 L1200 1400 L0 1400Z" fill="#eeeeee"/>
    <rect x="4" y="55" width="134" height="134" rx="14" fill="#f2f2f2"/>
    <rect x="1063" y="522" width="137" height="134" rx="14" fill="#f2f2f2"/>
  </svg>
</section>

<h2 class="section-title abs" style="top:777px;width:100%;text-align:center">Introducing Leaf Lattice</h2>
<p class="intro-text" style="top:864px">Leaf Lattice is a revolutionary, web-based application designed by Arborists to predict and improve tree preservation success. Do not trust the economic and environmental value of your trees to a vague "Rule of Thumb". Leaf Lattice provides certainty for these valuable assets.</p>

<div class="feature" style="left:187px">
  <svg width="40" height="44" viewBox="0 0 40 44"><path d="M20 44V8M20 30c-8 0-14-4-16-10 8 0 14 4 16 10zM20 22c8 0 13-4 15-10-8 0-13 4-15 10zM20 14c-5-2-7-6-6-12 5 2 7 6 6 12z" fill="#1a7a1a" stroke="#1a7a1a" stroke-width="3"/></svg>
  <p>Accurately Predict<br>Tree Survival</p>
</div>
<div class="feature" style="left:354px">
  <svg width="34" height="44" viewBox="0 0 34 44"><path d="M0 0h24l10 10v34H0z" fill="#1a7a1a"/><path d="M9 34c4-6 8-14 8-20M9 34c6-4 12-5 16-3" stroke="#fff" stroke-width="2.5" fill="none"/></svg>
  <p>Use Existing PDF<br>Site Plans</p>
</div>
<div class="feature" style="left:522px">
  <svg width="44" height="40" viewBox="0 0 44 40"><rect x="0" y="0" width="44" height="8" fill="#1a7a1a"/><rect x="0" y="16" width="32" height="8" fill="#1a7a1a"/><rect x="0" y="32" width="44" height="8" fill="#1a7a1a"/></svg>
  <p>Multi-Factor<br>Arborist Designed<br>Survival Algorithm</p>
</div>
<div class="feature" style="left:690px">
  <svg width="44" height="42" viewBox="0 0 44 42"><path d="M22 42V20C22 8 12 4 0 4c0 12 8 18 22 16M22 20c2-10 10-16 22-18-2 12-10 18-22 18z" fill="#1a7a1a" stroke="#1a7a1a" stroke-width="4"/></svg>
  <p>Adjust Plans For<br>Best Survivability</p>
</div>
<div class="feature" style="left:857px">
  <svg width="34" height="44" viewBox="0 0 34 44"><path d="M0 0h24l10 10v34H0z" fill="#1a7a1a"/><path d="M8 22h18M8 28h18M8 34h18" stroke="#fff" stroke-width="2.5"/></svg>
  <p>Print Certified<br>Reports For Clients</p>
</div>

<p class="intro-text" style="top:1189px">Leaf Lattice overlays your existing PDF site plans or tree preservation plans. Simply identify key existing structures and planned development. Our interactive Root Tracer system will show where the roots where likely to have spread.</p>

<h2 class="section-title abs" style="top:1445px;left:114px">Tree Preservation Reinvented</h2>

<article class="card" style="left:113px">
  <svg width="50" height="40" viewBox="0 0 50 40"><path d="M25 2A23 23 0 0 0 2 25v13h46V25A23 23 0 0 0 25 2z" fill="#3a3a3a"/><circle cx="25" cy="28" r="5" fill="#fff"/><path d="M25 28l8-16" stroke="#fff" stroke-width="3"/></svg>
  <h3>Multifactor Survival Analysis</h3>
  <p>Predict tree survival from root disruption with unparalleled accuracy. Our Predictive Analytics engine will overlay your development plan and instantly compute survival scores for each disrupted tree.</p>
  <div class="actions"><span class="btn btn-orange">Leaf Lattice Algorithm</span></div>
</article>
<article class="card" style="left:448px">
  <svg width="44" height="44" viewBox="0 0 44 44"><path d="M4 40l4-12L30 6l8 8-22 22z" fill="#3a3a3a"/><path d="M6 6l8-4 28 28-4 8z" fill="#3a3a3a" opacity=".85"/></svg>
  <h3>Arborist Designed</h3>
  <p>Leaf Lattice was designed by arborists, and our peer-reviewed algorithm packs over 30 years of top-flight client work and empirical observations into an easy to use web-based tool.</p>
  <div class="actions"><span class="btn btn-orange">Leaf Lattice Team</span></div>
</article>
<article class="card" style="left:783px">
  <svg width="54" height="42" viewBox="0 0 54 42"><rect x="6" y="2" width="42" height="30" fill="none" stroke="#3a3a3a" stroke-width="5"/><rect x="0" y="36" width="54" height="6" fill="#3a3a3a"/></svg>
  <h3>Point and Click Ease</h3>
  <p>Just upload your plan, choose any scale, add existing and new boundaries, drop trees on the map - and instantly receive an Arborist Certified survival score.</p>
  <div class="actions"><span class="btn btn-orange" style="padding:0 26px">Video</span><span class="btn btn-orange">Tutorial</span></div>
</article>

<section class="audience" role="img" aria-label="Photograph of tall tree trunks in a dense forest"></section>
<h2 class="audience-title">Leaf Lattice Is Perfect for</h2>

<div class="planner-card">
  <h3>Municipal Planners</h3>
  <ul>
    <li><span>&#10003;</span>Numerically assess viability of tree plans</li>
    <li><span>&#10003;</span>Simulate plan changes to increase survivability</li>
    <li><span>&#10003;</span>Arborist Expertise at Fraction of Price</li>
    <li><span>&#10003;</span>Enterprise Pricing</li>
  </ul>
</div>
<div class="photo" style="left:415px;width:379px;background:linear-gradient(160deg,#2e8a3c 0%,#d9d9d9 45%,#eeeeee 70%,#2a2a2a 100%)" role="img" aria-label="Photograph of a person in a green shirt unrolling site plan drawings"></div>
<div class="photo" style="left:818px;width:378px;background:linear-gradient(90deg,#6b5a3e 0%,#c9c6bc 45%,#d8d6cf 60%,#5e4a32 100%)" role="img" aria-label="Photograph of an arborist in a hard hat inspecting a tree trunk in a forest"></div>

</body>
</html>
```